VORN - Business cards

Business card to be created for Commercial sales staff

Target Market(s)

Commercial businesses

Industry/Entity Type

Commercial

Contact Information for Business Card

Look professional. For commercial clients

Colors
ffffff

Requirements
Must have
• - Vorn Logo
• - Commercial sales staff as postion
• - room for commerical sales manager role
• - person name and their mobile number
• - Website : vornelectrical.com.au
Nice to have
• White background.
• On back of business card just have the logo no other information
Should not have
• Should only have white background on front of card.

```html
<!DOCTYPE html>
<html lang="en">
<head>
<meta charset="utf-8">
<title>VORN – Business Cards</title>
<link rel="stylesheet" href="https://fonts.googleapis.com/css2?family=Jost:wght@300;400;600&display=swap">
<style>
  :root {
    --stage: #e4e4e4;
    --card-dark: #141414;
    --card-mid: #1f1f1f;
    --panel: #262626;
    --ink: #ffffff;
    --ink-soft: #d8d8d8;
    --rule: #8a8a8a;
    --accent: #d9222a;
  }
  * { box-sizing: border-box; margin: 0; padding: 0; }
  html, body {
    width: 1200px; height: 960px; overflow: hidden;
    background: var(--stage);
    font-family: "Jost", sans-serif;
  }
  .sheet {
    width: 1200px; height: 960px;
    display: flex; flex-direction: column; align-items: center; justify-content: center;
    gap: 44px;
  }
  .card {
    width: 720px; height: 412px;
    background: linear-gradient(160deg, var(--card-mid) 0%, var(--card-dark) 70%);
    box-shadow: 0 14px 30px rgba(0,0,0,.28);
    position: relative;
    color: var(--ink);
  }

  /* Back: brand only */
  .card--back { display: flex; align-items: center; justify-content: center; }
  .brand { display: flex; align-items: center; gap: 18px; }
  .brand__dot { width: 46px; height: 46px; border-radius: 50%; background: var(--accent); }
  .brand__name {
    font-weight: 600; font-size: 84px; letter-spacing: 4px; line-height: 1;
    color: var(--ink);
  }

  /* Front: person and contact */
  .person { position: absolute; top: 92px; left: 0; right: 0; text-align: center; }
  .person__name {
    font-weight: 400; font-size: 50px; letter-spacing: 16px; line-height: 1;
    padding-left: 16px;
  }
  .person__role {
    margin-top: 8px; font-weight: 400; font-size: 13px; letter-spacing: 4.5px;
    color: var(--ink-soft);
  }
  .contacts {
    position: absolute; left: 0; right: 0; bottom: 0; height: 170px;
    display: grid; grid-template-columns: 1fr 1fr 1fr;
  }
  .contact { position: relative; display: flex; flex-direction: column; align-items: center; }
  .contact + .contact::before {
    content: ""; position: absolute; left: 0; top: 62px; height: 56px;
    border-left: 1px solid var(--rule);
  }
  .contact__icon {
    width: 100%; height: 70px; display: flex; align-items: center; justify-content: center;
  }
  .contact--phone .contact__icon, .contact--web .contact__icon { background: var(--panel); }
  .contact--phone .contact__icon { margin-top: 20px; }
  .contact--mail .contact__icon { margin-top: 20px; background: transparent; }
  .contact--web .contact__icon { margin-top: 0; }
  .contact__icon svg { width: 20px; height: 20px; fill: var(--ink); }
  .contact__text {
    margin-top: 22px; font-size: 13px; letter-spacing: 3px; color: var(--ink-soft);
  }
  .contact--web .contact__text { margin-top: 42px; font-size: 12px; letter-spacing: 2.4px; }
</style>
</head>
<body>
<main class="sheet">

  <section class="card card--back" aria-label="Card back">
    <div class="brand">
      <span class="brand__dot"></span>
      <span class="brand__name">VORN</span>
    </div>
  </section>

  <section class="card card--front" aria-label="Card front">
    <div class="person">
      <h1 class="person__name">JOHN DOE</h1>
      <p class="person__role">COMMERCIAL SALES STAFF</p>
    </div>
    <div class="contacts">
      <div class="contact contact--phone">
        <div class="contact__icon">
          <svg viewBox="0 0 24 24" aria-hidden="true"><path d="M6.6 10.8a15.1 15.1 0 0 0 6.6 6.6l2.2-2.2c.3-.3.7-.4 1-.2 1.1.4 2.3.6 3.6.6.6 0 1 .4 1 1V20c0 .6-.4 1-1 1A17 17 0 0 1 3 4c0-.6.4-1 1-1h3.5c.6 0 1 .4 1 1 0 1.2.2 2.4.6 3.6.1.3 0 .7-.2 1z"/></svg>
        </div>
        <span class="contact__text">000.1234.5678</span>
      </div>
      <div class="contact contact--mail">
        <div class="contact__icon">
          <svg viewBox="0 0 24 24" aria-hidden="true"><path d="M3 6h18v12H3z M3 6l9 7 9-7" fill="var(--ink)"/><path d="M3.5 6.5l8.5 6.6 8.5-6.6" fill="none" stroke="var(--card-dark)" stroke-width="1.4"/></svg>
        </div>
        <span class="contact__text">johndoe@email.com</span>
      </div>
      <div class="contact contact--web">
        <div class="contact__icon">
          <svg viewBox="0 0 24 24" aria-hidden="true"><circle cx="12" cy="18" r="2"/><path d="M7 13.5a7 7 0 0 1 10 0l-1.5 1.5a5 5 0 0 0-7 0z"/><path d="M3.5 10a12 12 0 0 1 17 0L19 11.5a10 10 0 0 0-14 0z"/></svg>
        </div>
        <span class="contact__text">vornelectrical.com.au</span>
      </div>
    </div>
  </section>

</main>
</body>
</html>
```